Brimvale Solutions Website Project

We require a design to revamp and existing website for a company that provides online solutions for small the medium sized businesses including web development, online marketing, social media, online business plans, social media and e-commerce. We are looking to use colours that integrate well with the current logo. Our target market are small to medium sized businesses and individuals looking for a trusted adviser to cover all their online services.
Existing website - www.brimvalesolutions.com.au
Updates
Participation payments added.
Storyboard layout mentioned in brief was not attached in error. It will be uploaded shortly.
Storyboard file added.
Target Market(s)
Revamp of existing website - Looking for a professional design in line with the target market of small to medium businesses
Industry/Entity Type
Business
Requirements
Must have
- Refer the attached storyboard layout for the site design and requirements. Basic header, footer and sidebar are to be the same on every page with the content changing to match the requirements on each page. 8 pages in total
Should not have
- No click here text

```html
<!DOCTYPE html>
<html lang="en">
<head>
<meta charset="utf-8">
<title>Brimvale Solutions</title>
<link rel="stylesheet" href="https://fonts.googleapis.com/css2?family=Arimo:wght@400;700&family=Cabin:ital,wght@0,400;0,600;1,400&family=Dosis:wght@400;500&display=swap">
<style>
:root{
  --green:#7fb23a;
  --green-dark:#5f9a2a;
  --green-text:#2e7d12;
  --button:#1fb24a;
  --yellow:#f3f01c;
  --ink:#222;
  --body:#3a3a3a;
  --muted:#888;
  --line:#d6d6d6;
  --footer-top:#3c3c3c;
  --footer-bottom:#232323;
  --black:#050505;
  --icon-grey:#c9c9c9;
}
*{margin:0;padding:0;box-sizing:border-box}
html,body{width:821px;height:1200px;overflow:hidden;background:#fff}
body{position:relative;font-family:"Cabin",Arial,sans-serif;color:var(--body)}
.abs{position:absolute}
.top-strip{left:0;top:0;width:821px;height:5px;background:#e2e2e2}
.header{left:0;top:5px;width:821px;height:118px;background:linear-gradient(#fff,#f4f4f4)}
.brand{left:24px;top:38px;display:flex;align-items:center;gap:8px}
.brand-dot{width:30px;height:30px;border-radius:50%;background:var(--button)}
.brand-name{font-family:"Dosis",sans-serif;font-weight:500;font-size:20px;color:var(--green-text);line-height:1.05;width:110px}
.contact{right:20px;top:14px;font-family:"Dosis",sans-serif;font-size:14px;color:var(--ink)}
.contact b{font-weight:500;font-size:15px}
.social-top{right:20px;top:42px;display:flex;gap:3px}
.circle{width:26px;height:26px;border-radius:50%;background:radial-gradient(circle at 40% 35%,#fff,#d4d4d4);border:1px solid #bdbdbd}
.nav{left:401px;top:86px;height:37px;display:flex;border:1px solid #c8c8c8;border-bottom:0;background:linear-gradient(#fff,#eee)}
.nav a{display:flex;align-items:center;justify-content:center;font-family:"Dosis",sans-serif;font-size:14px;color:var(--ink);text-decoration:none;border-left:1px solid #c8c8c8}
.nav a:first-child{border-left:0}
.hero{left:0;top:123px;width:821px;height:231px;background:linear-gradient(90deg,#a8cf7a 0%,#8cbd48 38%,var(--green) 60%,var(--green-dark) 100%)}
.hero-photo{left:0;top:123px;width:320px;height:231px;background:radial-gradient(ellipse at 45% 45%,#e6dcc8 0%,#bfa98a 28%,#7fa85a 60%,rgba(140,189,72,0) 100%)}
.hero-title{left:300px;top:132px;width:500px;text-align:center;font-family:"Arimo",Arial,sans-serif;font-weight:700;font-size:41px;line-height:50px;color:#fff}
.hero-title em{font-style:normal;color:var(--yellow)}
.hero-sub{left:350px;top:244px;width:360px;text-align:center;font-family:"Arimo",Arial,sans-serif;font-size:22px;line-height:30px;color:#f6f6f6;font-weight:400}
.main{left:0;top:354px;width:578px;height:653px;background:linear-gradient(90deg,#fff 0%,#fafafa 100%)}
.band{left:0;width:578px;background:#fff;box-shadow:0 1px 3px rgba(0,0,0,.08)}
.service{width:190px}
.service-icon{flex:none;width:48px;height:56px;border-radius:6px;background:linear-gradient(#f6b73c,#e46a1e)}
.service h3{font-weight:400;font-size:11px;color:var(--ink);margin-bottom:1px}
.service p{font-size:9.5px;line-height:13.8px;color:#4a4a4a;width:125px}
.section-title{font-family:"Dosis",sans-serif;font-weight:500;font-size:16px;color:var(--ink)}
.work-box{left:17px;top:654px;width:544px;height:124px;background:#fff;border:1px solid #e6e6e6}
.thumb{top:667px;width:164px;height:98px;border:1px solid #9a9a9a}
.arrow{top:704px;width:26px;height:26px;border-radius:50%;background:#fff;border:1px solid #ccc}
.note{left:26px;top:793px;font-family:"Dosis",sans-serif;font-size:11.5px;color:var(--ink)}
.lorem{left:28px;top:826px;width:541px;font-size:10.3px;line-height:18.1px;text-align:justify;color:#222}
.sidebar{left:578px;top:354px;width:243px;height:653px;background:#fff;border-left:1px solid var(--line)}
.quote-head{left:579px;top:356px;width:242px;height:39px;background:linear-gradient(#fafafa,#e8e8e8);border-bottom:1px solid var(--line);font-family:"Dosis",sans-serif;font-size:16px;font-weight:500;color:var(--ink);padding:10px 18px}
.field{left:592px;width:213px;background:#fff;border:1px solid #d2d2d2;border-radius:4px;font-size:10px;font-style:italic;color:var(--muted);padding:6px 8px}
.submit{left:594px;top:579px;width:78px;height:24px;border-radius:3px;background:var(--button);color:#fff;font-size:11.5px;display:flex;align-items:center;justify-content:center}
.feed-title{left:597px;top:612px;font-family:"Dosis",sans-serif;font-size:16px;font-weight:500;color:var(--ink)}
.feed-icon{top:621px;width:22px;height:22px;border-radius:50%;background:var(--icon-grey)}
.feed-photo{left:598px;width:62px;height:62px;border:2px solid #e3e3e3;background:linear-gradient(#5f4a3c,#2e2a2a)}
.feed-text{left:671px;width:135px;font-size:9.5px;line-height:13.8px;color:#444}
.feed-name{left:598px;font-size:10px;font-weight:600;color:var(--green-text)}
.feed-time{left:740px;font-size:10px;font-weight:600;color:var(--green-text)}
.why{left:597px;top:816px;font-family:"Dosis",sans-serif;font-size:16px;font-weight:500;color:var(--ink)}
.why-text{left:597px;top:842px;width:208px;font-size:10.2px;line-height:17.8px;text-align:justify;color:#222}
.footer{left:0;top:1007px;width:821px;height:158px;background:linear-gradient(var(--footer-top),var(--footer-bottom))}
.footer h4{position:absolute;font-family:"Dosis",sans-serif;font-weight:500;font-size:14px;color:#fff}
.flink{font-size:9.5px;color:#e8e8e8}
.blog-text{left:398px;top:1039px;width:250px;font-size:9.3px;font-style:italic;line-height:15.7px;color:#ddd}
.author{left:397px;top:1108px;width:100px;height:21px;background:#111;border-radius:3px;color:#fff;font-size:10.5px;display:flex;align-items:center;justify-content:center}
.fcircle{top:1042px;width:25px;height:25px;border-radius:50%;background:radial-gradient(circle at 40% 35%,#fff,#cfcfcf)}
.bottom-bar{left:0;top:1165px;width:821px;height:35px;background:var(--black);color:#ddd;font-size:9.5px;padding:12px 18px}
</style>
</head>
<body>
<div class="abs top-strip"></div>
<header class="abs header"></header>
<div class="abs brand"><span class="brand-dot"></span><span class="brand-name">Brimvale Solutions</span></div>
<div class="abs contact"><b>265 555 0148</b> &nbsp;|&nbsp; hello@brimvalesolutions.com.au</div>
<div class="abs social-top"><span class="circle"></span><span class="circle"></span><span class="circle"></span></div>
<nav class="abs nav">
  <a style="width:67px">Home</a><a style="width:72px">About Us</a><a style="width:66px">Services</a><a style="width:73px">Portfolio</a><a style="width:49px">Blog</a><a style="width:73px">Contact</a>
</nav>

<section class="abs hero"></section>
<div class="abs hero-photo" role="img" aria-label="Hand holding a brass compass against a blurred green background"></div>
<h1 class="abs hero-title">Make <em>navigating</em> your<br>business online easy</h1>
<p class="abs hero-sub">We provide ongoing service to<br>ensure we are delivering the<br>best solution for your business</p>

<main class="abs main"></main>
<div class="abs band" style="top:356px;height:138px"></div>
<div class="abs band" style="top:499px;height:120px"></div>

<div class="abs service" style="left:17px;top:395px;display:flex;gap:8px"><div class="service-icon" role="img" aria-label="Figure working at a desk"></div><div><h3>Business</h3><p>Larkfield eSolutions provides you the Search Engine Optimization making your website.</p></div></div>
<div class="abs service" style="left:203px;top:395px;display:flex;gap:9px"><div class="service-icon" role="img" aria-label="Figure holding a light bulb"></div><div><h3>Marketing</h3><p>Larkfield eSolutions provides you the Search Engine Optimization making your website.</p></div></div>
<div class="abs service" style="left:388px;top:395px;display:flex;gap:6px"><div class="service-icon" role="img" aria-label="Figure with tools"></div><div><h3>Web Development</h3><p>Larkfield eSolutions provides you the Search Engine Optimization making your website.</p></div></div>
<div class="abs service" style="left:17px;top:514px;display:flex;gap:8px"><div class="service-icon" role="img" aria-label="Figure pushing a shopping cart"></div><div><h3>E-Commerce</h3><p>Larkfield eSolutions provides you the Search Engine Optimization making your website.</p></div></div>
<div class="abs service" style="left:212px;top:514px;display:flex;gap:5px"><div class="service-icon" style="width:43px" role="img" aria-label="Figure carrying blocks"></div><div><h3>Recent Blog</h3><p>Larkfield eSolutions provides you the Search Engine Optimization making your website.</p></div></div>
<div class="abs service" style="left:392px;top:514px;display:flex;gap:7px"><div class="service-icon" role="img" aria-label="Two figures with speech bubbles"></div><div><h3>Social Media</h3><p>Larkfield eSolutions provides you the Search Engine Optimization making your website.</p></div></div>

<h2 class="abs section-title" style="left:28px;top:625px">Our Recent Work</h2>
<div class="abs work-box"></div>
<div class="abs thumb" style="left:30px;background:linear-gradient(#dfe9cf,#b9a58a)" role="img" aria-label="Website screenshot of a food shop"></div>
<div class="abs thumb" style="left:207px;background:linear-gradient(#e9c0a4 0%,#fff 30%)" role="img" aria-label="Coming soon page for a marketing firm"></div>
<div class="abs thumb" style="left:382px;background:linear-gradient(90deg,#fff 25%,#d8d8d8 25%,#d8d8d8 75%,#fff 75%)" role="img" aria-label="Coming soon page for a design and photography studio"></div>
<div class="abs arrow" style="left:20px"><svg width="24" height="24" viewBox="0 0 24 24"><path d="M15 7 L8 12 L15 17 Z" fill="var(--button)"/></svg></div>
<div class="abs arrow" style="left:532px"><svg width="24" height="24" viewBox="0 0 24 24"><path d="M9 7 L16 12 L9 17 Z" fill="var(--button)"/></svg></div>
<p class="abs note">* More updates to the portfolio coming soon</p>
<div class="abs lorem">
<p>Lorem Ipsum is simply dummy text of the printing and typesetting industry. Lorem Ipsum has been the industry's standard dummy text ever since the 1500s, when an unknown printer took a galley of type and scrambled it to make a type specimen book. It has survived not only five centuries, but also the leap into electronic typesetting, remaining essentially unchanged. It was popularised in the 1960s with the release of Letraset sheets</p>
<p>Lorem Ipsum is simply dummy text of the printing and typesetting industry. Lorem Ipsum has been the industry's standard dummy text ever since the 1500s, when an unknown printer took a galley of type and scrambled it to make a type specimen book. It has survived not only five centuries, but also the leap into electronic typesetting, remaining essentially unchanged. It was popularised in the 1960s with the release of Letraset sheets</p>
</div>

<aside class="abs sidebar"></aside>
<div class="abs quote-head">Quick Quote</div>
<div class="abs field" style="top:404px;height:26px">Your name</div>
<div class="abs field" style="top:436px;height:26px">type your email address</div>
<div class="abs field" style="top:467px;height:26px">type your phone no.</div>
<div class="abs field" style="top:500px;height:69px">message</div>
<div class="abs submit">Submit Now</div>

<h2 class="abs feed-title">twittter feeds</h2>
<span class="abs feed-icon" style="left:746px"></span>
<span class="abs feed-icon" style="left:774px;border-radius:3px"></span>
<div class="abs feed-photo" style="top:641px" role="img" aria-label="Portrait photo of the author"></div>
<p class="abs feed-text" style="top:645px">Larkfield eSolutions provides you the Search Engine Optimi-zation making your website.</p>
<span class="abs feed-name" style="top:709px">Dana Whitlow</span>
<span class="abs feed-time" style="top:706px">11 hours ago</span>
<div class="abs feed-photo" style="top:731px" role="img" aria-label="Portrait photo of the author"></div>
<p class="abs feed-text" style="top:735px">Larkfield eSolutions provides you the Search Engine Optimi-zation making your website.</p>
<span class="abs feed-name" style="top:798px">Dana Whitlow</span>
<span class="abs feed-time" style="top:794px">11 hours ago</span>

<h2 class="abs why">Why Choose Us ?</h2>
<p class="abs why-text">Website solutions tailored to your business Cost effective pricing to suit your budget Strategies to support your online presence Regular maintenance packages available Professional design and development Online business plans to promote growth SEO techniques incorporated into all solutions Online marketing options available Blogs and e-commerce solutions available</p>

<footer class="abs footer">
  <h4 style="left:28px;top:9px">Quick Links</h4>
  <h4 style="left:398px;top:9px">Last Blog Post</h4>
  <h4 style="left:677px;top:9px">Social Media</h4>
</footer>
<div class="abs flink" style="left:28px;top:1040px;line-height:19px">Home Page<br>About Us<br>Services<br>Portfolio</div>
<div class="abs flink" style="left:107px;top:1040px;line-height:19px">E-Commerce<br>Web Development<br>Recent Blog<br>Quick Quote</div>
<div class="abs flink" style="left:215px;top:1040px;line-height:19px">Marketing<br>Business<br>Social Media</div>
<div class="abs flink" style="left:300px;top:1040px;line-height:21px">FAQ<br>Support<br>Contact</div>
<p class="abs blog-text">Our Website Design team give an unforgettable impression on the customers and the clients. We can assure you that this is the best place for requirement of yours regarding website design solutions</p>
<div class="abs author">BY Author Name</div>
<span class="abs fcircle" style="left:678px"></span>
<span class="abs fcircle" style="left:706px"></span>
<span class="abs fcircle" style="left:735px"></span>
<div class="abs bottom-bar">© 2012 Company Name &nbsp;|&nbsp; All right reserved</div>
</body>
</html>
```